Brindle Logistics Business Card Design

We are a trucking and warehousing company. We run freight in the US manly from the Pacific NW to TX and back up the the PNW. We also do warehousing where we store, move, and distribute freight. Looking for a clean and modern design of business card. We would like to look rich and elegant. Attached is our logo.

Industry/Entity Type

Trucking Company

Contact Information for Business Card

Looking for a clean and modern design of business card. We would like to look rich and elegant.

Font styles to use
Sans Serif

Colors

Designer to choose colors to be used in the design.

Requirements
Must have
• logo but it should not dominate the card
Should not have
• logo should not dominate the card

```html
<!DOCTYPE html>
<html lang="en">
<head>
<meta charset="utf-8">
<title>Brindle Logistics Business Card</title>
<link rel="stylesheet" href="https://fonts.googleapis.com/css2?family=Montserrat:wght@400;500;600;700&display=swap">
<style>
  :root {
    --backdrop: #2b2c2e;
    --card: #ffffff;
    --ink: #2f3033;
    --brand-blue: #0a6db3;
    --accent-orange: #f29a1f;
  }
  * { margin: 0; padding: 0; box-sizing: border-box; }
  html, body {
    width: 1200px; height: 900px; overflow: hidden;
    background: var(--backdrop);
    font-family: "Montserrat", sans-serif;
  }
  .stage {
    width: 1200px; height: 900px;
    display: flex; align-items: center; justify-content: center;
  }
  .card {
    position: relative;
    width: 1000px; height: 572px;
    background: var(--card);
    border-radius: 28px;
    overflow: hidden;
  }
  .card__wave { position: absolute; inset: 0; }
  .brand {
    position: absolute; left: 70px; top: 120px;
    display: flex; align-items: center; gap: 18px;
  }
  .brand__dot {
    width: 46px; height: 46px; border-radius: 50%;
    background: var(--brand-blue);
  }
  .brand__name {
    color: var(--ink);
    font-weight: 700; font-size: 40px; line-height: 1.05;
    letter-spacing: 1px; text-transform: uppercase;
  }
  .divider {
    position: absolute; left: 478px; top: 200px;
    width: 2px; height: 250px;
    background: var(--accent-orange);
  }
  .contact {
    position: absolute; left: 520px; top: 196px;
    color: var(--ink);
  }
  .contact__name {
    color: var(--brand-blue);
    font-weight: 600; font-size: 34px; letter-spacing: 2px;
    text-transform: uppercase;
  }
  .contact__role { font-size: 22px; margin-top: 2px; }
  .contact__address { font-size: 22px; line-height: 1.35; margin-top: 22px; }
  .contact__list { list-style: none; margin-top: 18px; font-size: 22px; line-height: 1.45; }
  .contact__item { display: flex; align-items: center; gap: 12px; }
  .contact__icon { width: 16px; height: 16px; flex: none; }
</style>
</head>
<body>
<main class="stage">
  <section class="card" aria-label="Business card front">
    <svg class="card__wave" viewBox="0 0 1000 572" preserveAspectRatio="none" aria-hidden="true">
      <path d="M0 300 C 220 300, 380 380, 520 470 C 640 545, 720 572, 800 572 L 0 572 Z" fill="var(--brand-blue)"/>
      <path d="M0 300 C 220 300, 380 380, 520 470 C 640 545, 720 572, 800 572 L 800 572 C 730 560, 650 530, 530 458 C 390 372, 230 290, 0 286 Z" fill="var(--accent-orange)"/>
      <path d="M0 312 C 220 312, 380 392, 520 482 C 640 556, 720 572, 800 572 L 0 572 Z" fill="var(--brand-blue)"/>
      <path d="M0 316 C 220 316, 380 396, 520 486 C 640 560, 720 572, 800 572 L 0 572 Z" fill="#ffffff" opacity="0"/>
    </svg>

    <div class="brand">
      <span class="brand__dot"></span>
      <span class="brand__name">Brindle<br>Logistics, LLC</span>
    </div>

    <div class="divider"></div>

    <div class="contact">
      <h1 class="contact__name">Daniel Carver</h1>
      <p class="contact__role">Founder</p>
      <p class="contact__address">2480 Harbor View Rd.<br>Tacoma, WA 98421</p>
      <ul class="contact__list">
        <li class="contact__item">
          <svg class="contact__icon" viewBox="0 0 16 16"><path d="M4 1 L6.5 4 L5 6 C6 8.5 7.5 10 10 11 L12 9.5 L15 12 L13 15 C7 14 2 9 1 3 Z" fill="var(--brand-blue)"/></svg>
          253-555-0148
        </li>
        <li class="contact__item">
          <svg class="contact__icon" viewBox="0 0 16 16"><rect x="1" y="3" width="14" height="10" rx="1.5" fill="none" stroke="var(--brand-blue)" stroke-width="1.6"/><path d="M1.5 4 L8 9 L14.5 4" fill="none" stroke="var(--brand-blue)" stroke-width="1.6"/></svg>
          info@brindlelogistics.com
        </li>
        <li class="contact__item">
          <svg class="contact__icon" viewBox="0 0 16 16"><circle cx="8" cy="8" r="7" fill="var(--brand-blue)"/><path d="M1 8 H15 M8 1 C5 4 5 12 8 15 M8 1 C11 4 11 12 8 15" fill="none" stroke="#fff" stroke-width="1"/></svg>
          www.brindlelogistics.com
        </li>
      </ul>
    </div>
  </section>
</main>
</body>
</html>
```